Corvana Edge Supplies - Stone Tooling Company

We need a round design for a saw blade that cuts stone.

We provide the tools and equipment necessary to cut, shape, polish granite-marble-engineered stone for your home.

Think designs on a skateboard wheel. Urban-street designs. We like something along the lines of something similar to the wheels on glimtrackrolls.com, snowboard designs etc..

2 Colors. Background - Matte Black. Gold print on top.
No shading/gradient as this has to be solid colors black/gold.
We would like the following text imbedded somewhere-
"Approved by Tall Morty"
"Granite/Engineered Stone"

Must have logo thats in the file

Target Market(s)

granite countertop fabricators- current designs are boring- we want this to stand out.

Industry/Entity Type

It Company

Font styles to use
Sans Serif
Decorative

Requirements
Must have
• Check attached picture. Something similar except with our attached logo, black background, and gold print.
Nice to have
• urban, street, skate, surf, tattoo, style
Should not have
• shadowing, unless by dots and lines for silk screen printing.

```html
<!DOCTYPE html>
<html lang="en">
<head>
<meta charset="utf-8">
<title>Corvana Edge Supplies – Fear Me When I Spin Blade</title>
<link rel="stylesheet" href="https://fonts.googleapis.com/css2?family=Anton&family=Oswald:wght@600&display=swap">
<style>
  :root {
    --page: #ffffff;
    --steel: #d9d6cc;
    --steel-edge: #bdb8a8;
    --slot: #ffffff;
    --gold: #efb53f;
    --black: #111111;
    --ink-white: #ffffff;
  }
  html, body {
    margin: 0;
    padding: 0;
    width: 1200px;
    height: 902px;
    overflow: hidden;
    background: var(--page);
  }
  .blade-canvas {
    display: block;
    width: 1200px;
    height: 902px;
  }
  .blade-steel { fill: var(--steel); stroke: var(--steel-edge); stroke-width: 3; }
  .blade-slot { stroke: var(--slot); stroke-width: 5; stroke-linecap: round; }
  .label-ring { fill: var(--gold); }
  .label-field { fill: var(--black); }
  .rose-art { fill: var(--gold); }
  .rock-art { fill: var(--gold); }
  .hub-ring { fill: var(--ink-white); stroke: var(--black); stroke-width: 4; }
  .arbor-hole { fill: var(--page); }
  .hub-band { fill: var(--black); }
  .headline {
    font-family: "Anton", "Oswald", sans-serif;
    font-size: 100px;
    letter-spacing: 3px;
    fill: var(--ink-white);
    stroke: var(--black);
    stroke-width: 4;
    paint-order: stroke;
  }
  .hub-text {
    font-family: "Oswald", sans-serif;
    font-weight: 600;
    font-size: 15px;
    letter-spacing: 1.5px;
    fill: var(--ink-white);
  }
  .brand-name {
    font-family: "Oswald", sans-serif;
    font-weight: 600;
    font-size: 26px;
    fill: var(--ink-white);
  }
</style>
</head>
<body>
<svg class="blade-canvas" viewBox="0 0 1200 902" xmlns="http://www.w3.org/2000/svg">
  <defs>
    <line id="slot" class="blade-slot" x1="600" y1="55" x2="600" y2="80"/>
    <path id="arc-top" d="M 414.6 375.1 A 200 200 0 0 1 733.8 301.4"/>
    <path id="arc-bottom" d="M 305.5 507.2 A 300 300 0 0 0 859.8 600"/>
    <path id="arc-hub-top" d="M 515 450 A 85 85 0 0 1 685 450"/>
    <path id="arc-hub-bottom" d="M 521 450 A 79 79 0 0 0 679 450"/>
  </defs>

  <g class="blade">
    <circle class="blade-steel" cx="600" cy="450" r="398"/>
    <g class="blade-slots">
      <use href="#slot" transform="rotate(0 600 450)"/>
      <use href="#slot" transform="rotate(15 600 450)"/>
      <use href="#slot" transform="rotate(30 600 450)"/>
      <use href="#slot" transform="rotate(45 600 450)"/>
      <use href="#slot" transform="rotate(60 600 450)"/>
      <use href="#slot" transform="rotate(75 600 450)"/>
      <use href="#slot" transform="rotate(90 600 450)"/>
      <use href="#slot" transform="rotate(105 600 450)"/>
      <use href="#slot" transform="rotate(120 600 450)"/>
      <use href="#slot" transform="rotate(135 600 450)"/>
      <use href="#slot" transform="rotate(150 600 450)"/>
      <use href="#slot" transform="rotate(165 600 450)"/>
      <use href="#slot" transform="rotate(180 600 450)"/>
      <use href="#slot" transform="rotate(195 600 450)"/>
      <use href="#slot" transform="rotate(210 600 450)"/>
      <use href="#slot" transform="rotate(225 600 450)"/>
      <use href="#slot" transform="rotate(240 600 450)"/>
      <use href="#slot" transform="rotate(255 600 450)"/>
      <use href="#slot" transform="rotate(270 600 450)"/>
      <use href="#slot" transform="rotate(285 600 450)"/>
      <use href="#slot" transform="rotate(300 600 450)"/>
      <use href="#slot" transform="rotate(315 600 450)"/>
      <use href="#slot" transform="rotate(330 600 450)"/>
      <use href="#slot" transform="rotate(345 600 450)"/>
    </g>
    <circle class="label-ring" cx="600" cy="450" r="348"/>
    <circle class="label-field" cx="600" cy="450" r="330"/>
  </g>

  <circle class="rose-art" cx="600" cy="440" r="192" role="img" aria-label="Gold tattoo-style rose in bloom behind the hub"/>

  <path class="rock-art" role="img" aria-label="Chunk of granite stone"
        d="M 322 380 L 360 368 L 390 392 L 396 438 L 383 468 L 338 476 L 310 450 L 312 406 Z"/>

  <text class="headline"><textPath href="#arc-top" startOffset="3%">FEAR ME</textPath></text>
  <text class="headline"><textPath href="#arc-bottom" startOffset="8%">WHEN I SPIN!</textPath></text>

  <g class="hub">
    <circle class="hub-band" cx="600" cy="450" r="100"/>
    <text class="hub-text"><textPath href="#arc-hub-top" startOffset="50%" text-anchor="middle">GRANITE / ENGINEERED STONE</textPath></text>
    <text class="hub-text"><textPath href="#arc-hub-bottom" startOffset="50%" text-anchor="middle">APPROVED BY TALL MORTY</textPath></text>
    <circle class="hub-ring" cx="600" cy="450" r="62"/>
    <circle class="arbor-hole" cx="600" cy="450" r="50"/>
  </g>

  <text class="brand-name" transform="translate(860 440) rotate(-80)" text-anchor="middle" dominant-baseline="middle">Corvana Edge Supplies</text>
</svg>
</body>
</html>
```